Big Room Track needs a CD cover!

I need a CD cover for a Big Room track which will be released soon. Please orientate at the cover of any existing track. It would be good to find a design which fits this. Its planned to generate a child of corporate design for upcoming releases. Please find a demo of the track and my logo to use in the cover. The name of the track is not found yet. Please use a short demo text to show where the title could be so I can add it afterwards.

Target Market(s)

Music streaming services. EDM Scene. Festival. Promotion.

Colors

Designer to choose colors to be used in the design.

Requirements
Must have
• Needs to be kind of a corporate design with the existing cover of another released track of mine. (Not the exact picture but use of logo and track title in this font). Needs to match the feel of the track (demo provided).
Nice to have
• Should reflect the energy of the track. Light colors are appreciated.
Should not have
• No kiddy pictures (like comic or something).

```html
<!DOCTYPE html>
<html lang="en">
<head>
<meta charset="utf-8">
<title>Solverance – Release Cover</title>
<link rel="stylesheet" href="https://fonts.googleapis.com/css2?family=Russo+One&display=swap">
<style>
  :root {
    --stage: #565174;
    --cover-top: #0a5f80;
    --cover-bottom: #034761;
    --note-shade: #03344b;
    --disc-glow: #4fb2f5;
    --disc-mid: #1662a8;
    --disc-edge: #03183a;
    --spray-dark: #071c33;
    --arc: rgba(90, 170, 220, 0.35);
    --logo: #e9f2f7;
  }
  * { margin: 0; padding: 0; box-sizing: border-box; }
  html, body {
    width: 1200px;
    height: 900px;
    overflow: hidden;
    background: var(--stage);
  }
  .canvas {
    position: relative;
    width: 1200px;
    height: 900px;
    display: flex;
    align-items: center;
    justify-content: center;
  }
  .cover {
    position: relative;
    width: 780px;
    height: 780px;
    background: linear-gradient(180deg, var(--cover-top) 0%, var(--cover-bottom) 100%);
    overflow: hidden;
  }
  .cover__arcs {
    position: absolute;
    inset: 0;
    width: 780px;
    height: 780px;
  }
  .cover__big-note {
    position: absolute;
    left: 68px;
    top: 31px;
    width: 155px;
    height: 360px;
    border-radius: 90px 10px 8px 60px;
    background: linear-gradient(200deg, var(--note-shade) 0%, rgba(3, 52, 75, 0.25) 100%);
    opacity: 0.8;
  }
  .cover__spray {
    position: absolute;
    left: 420px;
    top: -10px;
    width: 380px;
    height: 520px;
    border-radius: 60% 40% 30% 70% / 40% 40% 60% 60%;
    background: radial-gradient(ellipse at 25% 85%, rgba(7, 28, 51, 0.95) 0%, rgba(7, 28, 51, 0.55) 30%, rgba(7, 28, 51, 0) 72%);
  }
  .cover__wave {
    position: absolute;
    left: 160px;
    top: 410px;
    width: 140px;
    height: 74px;
    border-radius: 40px;
    background: radial-gradient(ellipse at 70% 50%, rgba(79, 178, 245, 0.6) 0%, rgba(79, 178, 245, 0) 70%);
  }
  .cover__record {
    position: absolute;
    left: 221px;
    top: 285px;
    width: 324px;
    height: 324px;
    border-radius: 50%;
    background: radial-gradient(circle at 42% 50%, var(--disc-glow) 0%, var(--disc-mid) 32%, #0a3a72 62%, var(--disc-edge) 100%);
    box-shadow: 0 44px 40px -28px rgba(0, 20, 35, 0.65), 0 0 40px rgba(79, 178, 245, 0.25);
  }
  .cover__logo {
    position: absolute;
    left: 0;
    right: 0;
    top: 664px;
    text-align: center;
    font-family: "Russo One", sans-serif;
    font-size: 42px;
    line-height: 1;
    letter-spacing: 1px;
    color: var(--logo);
  }
</style>
</head>
<body>
  <main class="canvas">
    <section class="cover">
      <svg class="cover__arcs" viewBox="0 0 780 780" aria-hidden="true">
        <path d="M455 285 C 540 160, 660 100, 790 60" fill="none" stroke="var(--arc)" stroke-width="2"/>
        <path d="M470 330 C 560 240, 680 190, 790 175" fill="none" stroke="var(--arc)" stroke-width="2"/>
        <path d="M520 300 C 600 270, 700 250, 790 245" fill="none" stroke="var(--arc)" stroke-width="1.5"/>
      </svg>
      <div class="cover__big-note" role="img" aria-label="Large faint eighth note in the background"></div>
      <div class="cover__spray" role="img" aria-label="Music notes and clefs bursting away from the record"></div>
      <div class="cover__wave" role="img" aria-label="Glowing blue sound wave running into the record"></div>
      <div class="cover__record" role="img" aria-label="Vinyl record with a glowing blue sound wave across it"></div>
      <p class="cover__logo">SOLVERANCE</p>
    </section>
  </main>
</body>
</html>
```